Preferred pricing vendor

We are a plumbing company that has many services
-Boilers & Controls
-Plumbing & Heating
-HVAC & Refrigeration
-Preventative Maintenacne
-Gas fitting & Drain Cleaning

We primarily look after condo buildings, and our preferred service rates ($98, $93, or $88 depending on the contract) extend to all of our clients. So in essence, we look after the mechanical room and common equipment but our clients can call us in for drain cleaning or replacing a fixture in their suite. The discounted rates apply to the personal residence. We want a flyer to let them know they get a discount on our services. A one-pager we can send out to all of our contract clients.

Included source files for our letterhead and logo just so you can see the colours we go with.

Target Market(s)

Residential repairs, individual people, replacement of fixtures in-suite specific repairs

Requirements
Must have
• be colourful and attractive

```html
<!DOCTYPE html>
<html lang="en">
<head>
<meta charset="utf-8">
<title>Keystone Mechanical Inc – Service Discount Flyer</title>
<link rel="stylesheet" href="https://fonts.googleapis.com/css2?family=Barlow+Condensed:ital,wght@0,600;0,700;1,700;1,800&family=Anton&family=Lexend:wght@500&display=swap">
<style>
  :root {
    --ink: #0b0b0b;
    --ink-glow: #2a2a2a;
    --brand-blue: #1f74c6;
    --wave-blue: #0a6fd1;
    --brand-orange: #f05a28;
    --headline-yellow: #ffe600;
    --burst-red: #ff0000;
    --tick-green: #28d49a;
    --white: #ffffff;
    --shadow-grey: #7a7a7a;
    --photo-navy: #1f2c4f;
    --photo-skin: #b98a72;
  }
  * { margin: 0; padding: 0; box-sizing: border-box; }
  html, body { width: 848px; height: 1200px; overflow: hidden; background: var(--ink); }
  .flyer {
    position: relative; width: 848px; height: 1200px; overflow: hidden;
    background: radial-gradient(ellipse at 55% 40%, var(--ink-glow) 0%, var(--ink) 60%);
  }
  .band { position: absolute; height: 30px; }
  .band--top-blue { top: 0; left: 0; width: 562px; background: var(--brand-blue); }
  .band--top-orange { top: 0; left: 568px; right: 0; background: var(--brand-orange); }
  .band--bottom-blue { bottom: 0; left: 0; width: 562px; background: var(--brand-blue); }
  .band--bottom-orange { bottom: 0; left: 562px; right: 0; background: var(--brand-orange); }

  .headline {
    position: absolute; inset: 0; pointer-events: none;
    font-family: "Barlow Condensed", sans-serif; font-style: italic; font-weight: 800;
    color: var(--headline-yellow); text-transform: uppercase; line-height: 1;
  }
  .headline span { position: absolute; display: block; white-space: nowrap; }
  .headline__big { left: 72px; top: 80px; font-size: 175px; letter-spacing: -3px; }
  .headline__line { left: 58px; top: 243px; font-size: 61px; letter-spacing: -0.5px; }
  .headline__mid { left: 72px; top: 291px; font-size: 140px; letter-spacing: -4px; }
  .headline__end { left: 58px; top: 419px; font-size: 77px; letter-spacing: -0.5px; }

  .brand { position: absolute; left: 520px; top: 92px; width: 290px; text-align: center; }
  .brand__dot { width: 64px; height: 64px; border-radius: 50%; background: var(--brand-orange); margin: 0 auto 18px; }
  .brand__name {
    font-family: "Barlow Condensed", sans-serif; font-weight: 700; font-size: 34px;
    line-height: 1.05; color: var(--brand-blue); letter-spacing: 1px; text-transform: uppercase;
  }

  .services { position: absolute; left: 61px; top: 541px; height: 185px; padding-left: 40px; border-left: 27px solid var(--brand-blue); list-style: none; }
  .services li {
    display: flex; align-items: center; gap: 11px; height: 37px; white-space: nowrap;
    font-family: "Lexend", sans-serif; font-weight: 500; font-size: 18px; color: var(--white);
  }
  .services svg { width: 20px; height: 20px; flex: none; }

  .photo { position: absolute; }
  .photo--technician { left: 448px; top: 333px; width: 373px; height: 482px; border-radius: 120px 120px 0 0;
    background: linear-gradient(180deg, var(--photo-skin) 0%, var(--photo-navy) 35%, var(--photo-navy) 100%); }
  .photo--van { left: 386px; top: 808px; width: 444px; height: 173px; border-radius: 30px 40px 12px 12px;
    background: linear-gradient(180deg, #f3f3f3 0%, #dcdcdc 80%, #3a3a3a 100%); }

  .waves { position: absolute; inset: 0; }

  .burst { position: absolute; left: 0; top: 722px; width: 450px; height: 465px; }
  .burst__text {
    position: absolute; left: 92px; top: 818px; transform: rotate(-9deg); transform-origin: left top;
    font-family: "Anton", sans-serif; color: var(--white); text-transform: uppercase;
    line-height: 0.98; text-shadow: 3px 3px 0 var(--shadow-grey), 5px 5px 0 var(--shadow-grey);
  }
  .burst__text span { display: block; font-size: 68px; white-space: nowrap; }

  .rates { position: absolute; right: 22px; top: 1102px; text-align: right; color: var(--white);
    font-family: "Barlow Condensed", sans-serif; text-transform: uppercase; white-space: nowrap; }
  .rates__title { font-style: italic; font-weight: 800; font-size: 38px; line-height: 1; }
  .rates__detail { font-weight: 700; font-size: 24px; line-height: 1.2; margin-top: 6px; }
</style>
</head>
<body>
<main class="flyer">
  <div class="band band--top-blue"></div>
  <div class="band band--top-orange"></div>

  <svg class="waves" viewBox="0 0 848 1200" aria-hidden="true">
    <path d="M0 773 L150 800 L848 900 L848 1100 L0 1100 Z" fill="var(--wave-blue)"/>
    <path d="M0 970 C300 1010 500 1060 700 1080 C780 1090 820 1085 848 1078 L848 1200 L0 1200 Z" fill="var(--brand-orange)"/>
  </svg>

  <div class="photo photo--technician" role="img" aria-label="Photo of a smiling plumber in navy overalls and cap holding a wrench and a pipe wrench"></div>

  <h1 class="headline">
    <span class="headline__big">We Are</span>
    <span class="headline__line">A Plumbing Company</span>
    <span class="headline__mid">That Has</span>
    <span class="headline__end">Many Services</span>
  </h1>

  <div class="brand">
    <div class="brand__dot"></div>
    <p class="brand__name">Keystone<br>Mechanical Inc</p>
  </div>

  <ul class="services">
    <li><svg viewBox="0 0 20 20"><rect x="2" y="3" width="15" height="15" rx="2" fill="none" stroke="var(--tick-green)" stroke-width="2.4"/><path d="M5 10 L9 14 L18 3" fill="none" stroke="var(--tick-green)" stroke-width="2.6"/></svg>Boilers &amp; Controls</li>
    <li><svg viewBox="0 0 20 20"><rect x="2" y="3" width="15" height="15" rx="2" fill="none" stroke="var(--tick-green)" stroke-width="2.4"/><path d="M5 10 L9 14 L18 3" fill="none" stroke="var(--tick-green)" stroke-width="2.6"/></svg>Plumbing &amp; Heating</li>
    <li><svg viewBox="0 0 20 20"><rect x="2" y="3" width="15" height="15" rx="2" fill="none" stroke="var(--tick-green)" stroke-width="2.4"/><path d="M5 10 L9 14 L18 3" fill="none" stroke="var(--tick-green)" stroke-width="2.6"/></svg>HVAC &amp; Refrigeration</li>
    <li><svg viewBox="0 0 20 20"><rect x="2" y="3" width="15" height="15" rx="2" fill="none" stroke="var(--tick-green)" stroke-width="2.4"/><path d="M5 10 L9 14 L18 3" fill="none" stroke="var(--tick-green)" stroke-width="2.6"/></svg>Preventative Maintenacne</li>
    <li><svg viewBox="0 0 20 20"><rect x="2" y="3" width="15" height="15" rx="2" fill="none" stroke="var(--tick-green)" stroke-width="2.4"/><path d="M5 10 L9 14 L18 3" fill="none" stroke="var(--tick-green)" stroke-width="2.6"/></svg>Gas fitting &amp; Drain Cleaning</li>
  </ul>

  <div class="photo photo--van" role="img" aria-label="Photo of a white company service van"></div>

  <svg class="burst" viewBox="-230 -235 460 470" aria-hidden="true">
    <polygon transform="rotate(4)" fill="var(--burst-red)" points="225,0 186,29 214,70 168,85 182,132 133,133 132,182 85,168 70,214 29,186 0,225 -29,186 -70,214 -85,168 -132,182 -133,133 -182,132 -168,85 -214,70 -186,29 -225,0 -186,-29 -214,-70 -168,-85 -182,-132 -133,-133 -132,-182 -85,-168 -70,-214 -29,-186 0,-225 29,-186 70,-214 85,-168 132,-182 133,-133 182,-132 168,-85 214,-70 186,-29"/>
  </svg>
  <p class="burst__text"><span>Special</span><span>Discount</span><span>Available</span></p>

  <div class="rates">
    <p class="rates__title">Service Rates:</p>
    <p class="rates__detail">($98, $93, or $88 depending on the contract)</p>
  </div>

  <div class="band band--bottom-blue"></div>
  <div class="band band--bottom-orange"></div>
</main>
</body>
</html>
```